Vento Designs would like to have an appealing package box for kitchen utensils.

This kitchen product will be introduced to the market so a package box design is needed for a silicone kitchen utensils. This is a set of 5 green pieces of kitchen utensils that will come with an additional one for free. This free additional utensil is a whisk egg that is not the same colour of the rest utensils which make a little different but attractive to the utensils set.
Photos have been provided so is the logo from the business. There are two colours of the logo, I do not have preferences with colours of the logo but I would like to see on both colours to see which one looks better.
Target Market(s)
Everyone
Requirements
Must have
- Some kitchen background images like some pots sitting on a cooktop or microwave or fruits and vegetables, something to combine with the kitchen utensils and attract customers.
- BPA free should be quoted on front side of the package box
Nice to have
- An small description of each kitchen utensil should be added in one of the sides of the package box.
Should not have
- Not many colours should be involved on the package box design.

```html
<!DOCTYPE html>
<html lang="en">
<head>
<meta charset="utf-8">
<title>Vento Designs – Mixing Spoon Box Dieline</title>
<link href="https://fonts.googleapis.com/css2?family=Oswald:wght@400;600&family=Montserrat:wght@400;600&family=Great+Vibes&display=swap" rel="stylesheet">
<style>
  :root{
    --teal:#2e9e97;
    --panel:#ebebed;
    --paper:#ffffff;
    --ink:#1b1b1b;
    --white:#ffffff;
    --spoon-green:#9fd06a;
    --glue:#f4f4f4;
  }
  html,body{margin:0;padding:0;width:858px;height:1200px;overflow:hidden;background:var(--paper);}
  .dieline{display:block;width:858px;height:1200px;}
  .size-note{font-family:"Montserrat",sans-serif;font-size:20px;fill:var(--ink);}
  .side-copy{font-family:"Oswald",sans-serif;font-size:9.5px;fill:var(--white);text-anchor:middle;}
  .script{font-family:"Great Vibes",cursive;}
  .spaced{font-family:"Montserrat",sans-serif;letter-spacing:7px;}
  .small-caps{font-family:"Montserrat",sans-serif;font-weight:600;}
  .feature-title{font-family:"Oswald",sans-serif;font-weight:600;font-size:11px;fill:var(--white);}
  .feature{font-family:"Oswald",sans-serif;font-size:9.5px;fill:var(--white);}
  .brand-name{font-family:"Montserrat",sans-serif;font-weight:600;text-anchor:middle;}
  .size-list{font-family:"Oswald",sans-serif;font-size:6px;fill:var(--ink);text-anchor:middle;}
</style>
</head>
<body>
<svg class="dieline" viewBox="0 0 965 1350" preserveAspectRatio="none" xmlns="http://www.w3.org/2000/svg">
  <defs>
    <linearGradient id="kitchenScene" x1="0" y1="0" x2="1" y2="1">
      <stop offset="0" stop-color="#3a2a22"/>
      <stop offset="0.45" stop-color="#b5532c"/>
      <stop offset="0.75" stop-color="#4f6a2e"/>
      <stop offset="1" stop-color="#1d1a18"/>
    </linearGradient>
    <linearGradient id="utensilSet" x1="0" y1="0" x2="0" y2="1">
      <stop offset="0" stop-color="#cfe9b4"/>
      <stop offset="1" stop-color="#b9c6d3"/>
    </linearGradient>
    <linearGradient id="spoonFill" x1="0" y1="0" x2="0" y2="1">
      <stop offset="0" stop-color="#f2f5ee"/>
      <stop offset="0.6" stop-color="#9fd06a"/>
      <stop offset="1" stop-color="#e4e8df"/>
    </linearGradient>
  </defs>

  <text class="size-note" x="80" y="62">85x65x295mm</text>

  <!-- Back panel with glue flap -->
  <g class="back-panel">
    <rect x="35" y="268" width="283" height="824" fill="var(--glue)" stroke="#dcdcdc"/>
    <rect x="78" y="268" width="240" height="824" fill="var(--paper)"/>
    <polygon points="78,268 318,268 318,578 78,760" fill="url(#kitchenScene)" role="img" aria-label="Photo of vegetables simmering in a pot with a green silicone spoon"/>
    <rect x="80" y="750" width="230" height="232" fill="url(#utensilSet)" opacity="0.7" rx="6" role="img" aria-label="Photo of the five green silicone utensils standing in a holder"/>
    <text class="script" x="192" y="1010" font-size="19" text-anchor="middle" fill="var(--ink)">complete the 5 piece set</text>
    <text class="size-list" x="200" y="1034">LADLE 28 * 8.5cm 86G</text>
    <text class="size-list" x="200" y="1042">SPOONULA 28 * 5.8cm 70G</text>
    <text class="size-list" x="200" y="1050">MIXING SPOON 27 * 5.8cm 80G</text>
    <text class="size-list" x="200" y="1058">SPATULA 28 * 5.5cm 75G</text>
    <text class="size-list" x="200" y="1067">SPATULA / TURNER 29 * 8cm 85G</text>
  </g>

  <!-- Left side panel -->
  <g class="side-panel-left">
    <polygon points="318,262 328,212 336,188 494,188 494,1172 336,1172 328,1148 318,1092" fill="var(--teal)"/>
    <text class="side-copy" x="405" y="424">ENJOY COOKING AGAIN WITH</text>
    <text class="side-copy" x="405" y="460">THESE SUPER CUTE KITCHEN</text>
    <text class="side-copy" x="405" y="496">UTENSILS, GUARANTEED TO ADD</text>
    <text class="side-copy" x="405" y="532">FUN TO YOUR KITCHEN AS WELL</text>
    <text class="side-copy" x="405" y="568">AS BEING TOUGH ENOUGH TO</text>
    <text class="side-copy" x="405" y="604">LAST A LIFETIME.</text>
    <text class="side-copy" x="405" y="676">IS COOKING NO LONGER FUN?</text>
    <text class="side-copy" x="405" y="712">HAS ALL THE ENJOYMENT</text>
    <text class="side-copy" x="405" y="748">DRAINED OUT OF YOUR KITCHEN?</text>
    <text class="side-copy" x="405" y="784">ARE YOU SICK OF REPLACING</text>
    <text class="side-copy" x="405" y="820">BROKEN UTENSILS?</text>
    <text class="script" transform="translate(396,1040) rotate(-90)" font-size="30" fill="var(--white)">Mixing Spoon</text>
    <text transform="translate(424,1012) rotate(-90)" font-family="Oswald,sans-serif" font-weight="600" font-size="11" fill="var(--white)">27 * 5.8cm 80g</text>
  </g>

  <!-- Front panel -->
  <g class="front-panel">
    <rect x="502" y="78" width="242" height="184" fill="var(--teal)"/>
    <rect x="502" y="262" width="242" height="836" fill="var(--panel)"/>
    <text class="brand-name" x="624" y="309" font-size="11" fill="var(--ink)">Vento Designs</text>
    <text class="spaced" x="623" y="353" font-size="11" text-anchor="middle" fill="var(--ink)">KITCHEN UTENSIL</text>
    <text class="script" x="624" y="382" font-size="30" text-anchor="middle" fill="var(--ink)">Mixing Spoon</text>
    <text class="small-caps" x="624" y="401" font-size="7.5" text-anchor="middle" fill="var(--ink)">PREMIUM SILICONE</text>
    <rect x="590" y="405" width="68" height="11" fill="var(--teal)"/>
    <text class="small-caps" x="624" y="413.5" font-size="6.5" letter-spacing="4" text-anchor="middle" fill="var(--white)">BPA FREE</text>
    <text x="624" y="429" font-family="Montserrat,sans-serif" font-size="8" letter-spacing="2" text-anchor="middle" fill="var(--teal)">1 PIECE SET</text>
    <rect x="578" y="460" width="110" height="505" rx="55" fill="url(#spoonFill)" role="img" aria-label="Photo of the green silicone mixing spoon"/>
    <text class="brand-name" x="624" y="1040" font-size="16" fill="var(--ink)">Vento Designs</text>
  </g>

  <!-- Bottom flap -->
  <g class="bottom-flap">
    <path d="M502,1098 H744 V1315 Q744,1325 734,1325 H512 Q502,1325 502,1315 Z" fill="var(--panel)" stroke="#d6d6d6"/>
    <text class="brand-name" x="624" y="1230" font-size="16" fill="var(--ink)">Vento Designs</text>
  </g>

  <!-- Right side panel -->
  <g class="side-panel-right">
    <polygon points="750,188 912,188 920,212 928,262 928,1092 920,1148 912,1172 750,1172" fill="var(--teal)"/>
    <text class="feature-title" x="773" y="418">FEATURES:</text>
    <g fill="var(--white)">
      <rect x="761" y="434" width="7" height="7"/><text class="feature" x="774" y="442">Absolute premium quality silicone</text>
      <rect x="761" y="458" width="7" height="7"/><text class="feature" x="774" y="466">Long lasting and incredibly strong</text>
      <rect x="761" y="481" width="7" height="7"/><text class="feature" x="774" y="489">Stain and odor resistant</text>
      <rect x="761" y="505" width="7" height="7"/><text class="feature" x="774" y="513">Easy to clean and dishwasher safe</text>
      <rect x="761" y="529" width="7" height="7"/><text class="feature" x="774" y="537">Balanced and comfortable grip</text>
      <rect x="761" y="552" width="7" height="7"/><text class="feature" x="774" y="560">Nylon core as strong as steel but</text>
      <text class="feature" x="774" y="572">won't corrode</text>
      <rect x="761" y="587" width="7" height="7"/><text class="feature" x="774" y="595">100% FDA food grade silicone</text>
      <rect x="761" y="611" width="7" height="7"/><text class="feature" x="774" y="619">Heat resistant to 480 degrees</text>
      <text class="feature" x="774" y="631">Fahrenheit</text>
      <text class="feature" x="774" y="643">(249 degrees Centigrade)</text>
      <rect x="761" y="658" width="7" height="7"/><text class="feature" x="774" y="666">11 to 11.5 inches in length</text>
    </g>
    <text class="spaced" transform="translate(814,950) rotate(-90)" font-size="10" fill="var(--white)">KITCHEN UTENSIL</text>
    <text class="script" transform="translate(846,912) rotate(-90)" font-size="30" fill="var(--white)">Mixing Spoon</text>
    <text class="small-caps" transform="translate(861,876) rotate(-90)" font-size="6.5" fill="var(--white)">PREMIUM SILICONE</text>
    <rect x="864" y="808" width="12" height="68" fill="none" stroke="var(--white)" stroke-width="1"/>
    <text class="small-caps" transform="translate(873,873) rotate(-90)" font-size="6" letter-spacing="3.5" fill="var(--white)">BPA FREE</text>
    <text transform="translate(889,876) rotate(-90)" font-family="Montserrat,sans-serif" font-size="7.5" letter-spacing="1.5" fill="var(--white)">1 PIECE SET</text>
    <text class="brand-name" x="841" y="1024" font-size="11" fill="var(--white)">Vento Designs</text>
  </g>
</svg>
</body>
</html>
```